" Será uma empresa de acessórios, equipamentos e assistência técnica para informática e celulares. Capas personalizadas, recuperação de dados, perícia técnica. "

```html
<!DOCTYPE html>
<html lang="pt-BR">
<head>
<meta charset="UTF-8">
<title>Cartão de Visita — Pixel Clinic</title>
<link href="https://fonts.googleapis.com/css2?family=Roboto:wght@400;700;900&display=swap" rel="stylesheet">
<style>
  :root {
    --navy: #1f3b57;
    --orange: #ec6a1f;
    --white: #ffffff;
    --paper: #f7f7f7;
    --ink: #1c2d40;
    --stage: #dfe2e5;
  }
  * { margin: 0; padding: 0; box-sizing: border-box; }
  html, body { width: 1200px; height: 1200px; overflow: hidden; }
  body {
    background: var(--stage);
    font-family: "Roboto", Arial, sans-serif;
    position: relative;
  }
  .card {
    position: absolute;
    left: 264px;
    width: 672px;
    height: 380px;
    overflow: hidden;
    box-shadow: 0 10px 24px rgba(0,0,0,.18);
  }
  .card--front { top: 256px; background: var(--navy); }
  .card--back {
    top: 684px;
    background: linear-gradient(135deg, var(--white) 0%, var(--paper) 60%, #ececec 100%);
  }

  .brand {
    display: flex;
    align-items: center;
    gap: 14px;
    position: absolute;
  }
  .brand__name {
    font-weight: 900;
    letter-spacing: 4px;
    text-transform: uppercase;
    white-space: nowrap;
  }
  .brand__dot { border-radius: 50%; background: var(--orange); flex: none; }

  .card--front .brand { left: 50%; top: 178px; transform: translate(-50%, -50%); }
  .card--front .brand__name { color: var(--white); font-size: 52px; }
  .card--front .brand__dot { width: 34px; height: 34px; }

  .front-rule {
    position: absolute;
    top: 352px;
    left: 0;
    height: 7px;
    width: 612px;
    background: var(--orange);
  }
  .front-rule--end { left: 618px; width: 44px; background: var(--white); }

  .card--back .brand { right: 40px; top: 92px; }
  .card--back .brand__name { color: var(--navy); font-size: 30px; letter-spacing: 3px; }
  .card--back .brand__dot { width: 20px; height: 20px; }

  .back-deco {
    position: absolute;
    right: 120px;
    top: 90px;
    width: 260px;
    height: 260px;
    border-radius: 50%;
    background: var(--orange);
    opacity: .07;
  }

  .icon-rail {
    position: absolute;
    left: 0; top: 0; bottom: 0;
    width: 46px;
    background: var(--navy);
  }
  .contact {
    position: absolute;
    left: 0;
    display: flex;
    align-items: center;
  }
  .contact__icon {
    width: 46px;
    display: flex;
    justify-content: center;
    flex: none;
  }
  .contact__icon svg { width: 22px; height: 22px; }
  .contact__text {
    margin-left: 18px;
    color: var(--ink);
    font-weight: 700;
    line-height: 1.25;
  }
  .contact--email { top: 78px; }
  .contact--email .contact__text { font-size: 22px; }
  .contact--phone { top: 130px; }
  .contact--phone .contact__text { font-size: 17px; }
  .contact--web { top: 192px; }
  .contact--web .contact__text { font-size: 22px; }
  .contact--address { top: 256px; }
  .contact--address .contact__text { font-size: 14px; }
</style>
</head>
<body>

<section class="card card--front" aria-label="Frente do cartão">
  <div class="brand">
    <span class="brand__dot"></span>
    <span class="brand__name">Pixel Clinic</span>
  </div>
  <div class="front-rule"></div>
  <div class="front-rule front-rule--end"></div>
</section>

<section class="card card--back" aria-label="Verso do cartão">
  <div class="back-deco"></div>
  <div class="icon-rail"></div>

  <div class="brand">
    <span class="brand__dot"></span>
    <span class="brand__name">Pixel Clinic</span>
  </div>

  <div class="contact contact--email">
    <span class="contact__icon">
      <svg viewBox="0 0 24 24" fill="none" stroke="#fff" stroke-width="2"><rect x="3" y="5" width="18" height="14" rx="2"/><path d="M3 7l9 6 9-6"/></svg>
    </span>
    <span class="contact__text">empresa@.com.br</span>
  </div>

  <div class="contact contact--phone">
    <span class="contact__icon">
      <svg viewBox="0 0 24 24" fill="#fff"><path d="M6.6 10.8a15 15 0 006.6 6.6l2.2-2.2a1 1 0 011-.25 11 11 0 003.5.56 1 1 0 011 1V20a1 1 0 01-1 1A17 17 0 013 4a1 1 0 011-1h3.5a1 1 0 011 1 11 11 0 00.56 3.5 1 1 0 01-.25 1z"/></svg>
    </span>
    <span class="contact__text">(11) 0000-0000<br>(11) 00000-0000</span>
  </div>

  <div class="contact contact--web">
    <span class="contact__icon">
      <svg viewBox="0 0 24 24" fill="none" stroke="#fff" stroke-width="1.8"><circle cx="12" cy="12" r="9"/><path d="M3 12h18M12 3c3 3 3 15 0 18M12 3c-3 3-3 15 0 18"/></svg>
    </span>
    <span class="contact__text">www.empresa.com.br</span>
  </div>

  <div class="contact contact--address">
    <span class="contact__icon">
      <svg viewBox="0 0 24 24" fill="#fff"><path d="M12 2a7 7 0 00-7 7c0 5 7 13 7 13s7-8 7-13a7 7 0 00-7-7zm0 9.5A2.5 2.5 0 1112 6.5a2.5 2.5 0 010 5z"/></svg>
    </span>
    <span class="contact__text">Rua do projeto, 00 Centro - Cidade - Estado<br>Cep. 00.000.000</span>
  </div>
</section>

</body>
</html>
```